BrPeople Business Cards for SME Experts

We need a business card for a new company based in Clearwater FL called Brightfold of People. BrP is your access to on-demand subject matter experts. The final design should be very clean communicating innovation and expertise. Our logo design is attached.

The Information Age has affected the workforce in that automation and computerization have resulted in higher productivity coupled with net job loss of many knowledgeable employees. Combined with the creation of the internet and search capabilities, the disintermediation of the value chain of Subject Matter Experts (SME) has happened. We no longer need to work through traditional consulting firms for all consulting needs, instead the direct access to the SME, through a leaner and lower cost model is what the market is demanding.
BrPeople is a new marketplace to buy consulting services. The business model is that all consultants (subject matter experts) can become a consulting resource in the marketplace following our guidelines. The consumer can now easily access consultants that they could not find easily before.
In much the way an Zaxo car can be identified and requested, so can a BrPeople Consultant. Each consultant can be identified by: location, expertise, billing rate, and prior experience rating.
By seamlessly connecting consultants to requesters through a new Brightfold of People marketplace, you now will have an easy to use and quicker turnaround to request and staff your consulting needs. Leveraging the BrP app, you can access the subject matter expert you need for your business requirement.

Target Market(s)

Small and medium sized companies; non-profits

Industry/Entity Type

Business Consultant

Contact Information for Business Card

Name
website
email address
Logo
mailing address (debating if I really need...)
twitter
LinkedIn

Requirements
Must have
• the logo I have included in the design; want the colors to be consistent with the logo design

```html
<!DOCTYPE html>
<html lang="en">
<head>
<meta charset="utf-8">
<title>Brightfold of People — Business Card</title>
<link href="https://fonts.googleapis.com/css2?family=Source+Sans+3:wght@400;600;700&display=swap" rel="stylesheet">
<style>
  :root {
    --backdrop: #e9e9e7;
    --card: #fbfbfb;
    --teal: #2db4d6;
    --teal-deep: #1c9cc0;
    --indigo: #3a3aa0;
    --ink: #3c3c3c;
    --ink-soft: #6a6a6a;
    --divider: #a9d8ea;
  }
  * { box-sizing: border-box; margin: 0; padding: 0; }
  html, body {
    width: 1200px; height: 1023px; overflow: hidden;
    background: var(--backdrop);
    font-family: "Source Sans 3", "Helvetica Neue", Arial, sans-serif;
  }
  .business-card {
    position: absolute; left: 100px; top: 226px;
    width: 1000px; height: 572px;
    background: var(--card);
    border-radius: 6px;
    box-shadow: 0 10px 30px rgba(0,0,0,0.12);
  }
  .card-divider {
    position: absolute; left: 500px; top: 175px;
    width: 1px; height: 220px;
    background: var(--divider);
  }
  .edge-tab {
    position: absolute; left: 690px; top: 548px;
    width: 150px; height: 46px;
    background: linear-gradient(var(--teal), var(--teal-deep));
    border-radius: 12px;
    box-shadow: inset 0 -4px 0 rgba(0,0,0,0.08);
  }
  .contact-block {
    position: absolute; left: 72px; top: 200px;
    color: var(--ink);
  }
  .person-name {
    font-size: 40px; font-weight: 600; color: var(--teal);
    line-height: 1;
  }
  .person-title {
    font-size: 22px; color: var(--ink); margin-top: 6px;
  }
  .contact-list { list-style: none; margin-top: 18px; }
  .contact-list li {
    display: flex; align-items: center; gap: 14px;
    font-size: 21px; line-height: 32px; color: var(--ink-soft);
  }
  .contact-marker {
    width: 20px; height: 20px; border-radius: 4px;
    background: var(--teal); flex: none;
  }
  .mailing-address {
    font-style: normal; margin-top: 18px;
    font-size: 21px; line-height: 28px; color: var(--ink-soft);
  }
  .brand-lockup {
    position: absolute; left: 500px; top: 0; width: 500px; height: 572px;
    display: flex; flex-direction: column; align-items: center; justify-content: center;
    gap: 22px;
  }
  .brand-circle {
    width: 110px; height: 110px; border-radius: 50%;
    border: 7px solid var(--teal);
  }
  .brand-name {
    font-size: 40px; font-weight: 700; color: var(--indigo);
    letter-spacing: 0.5px;
  }
</style>
</head>
<body>
  <section class="business-card" aria-label="Brightfold of People business card">
    <div class="contact-block">
      <h1 class="person-name">Dorian Vale</h1>
      <p class="person-title">Managing Director</p>
      <ul class="contact-list">
        <li><span class="contact-marker"></span>hello@brightfoldpeople.com</li>
        <li><span class="contact-marker"></span>www.brightfoldpeople.com</li>
        <li><span class="contact-marker"></span>@dorianvale_brp</li>
        <li><span class="contact-marker"></span>dorianvale</li>
      </ul>
      <address class="mailing-address">480 Harbor Palm Drive<br>Clearwater, FL 33755</address>
    </div>

    <div class="card-divider"></div>

    <div class="brand-lockup">
      <div class="brand-circle"></div>
      <div class="brand-name">Brightfold of People</div>
    </div>

    <div class="edge-tab"></div>
  </section>
</body>
</html>
```